依頼概要
■依頼の目的/概要
インフルエンザワクチンのポスターを作成して頂きたいです。
クリニック内の待合室に掲示します。

■依頼詳細
A2サイズです。
温かみのある柔らかいデザインをお願いします。
ポスターには、人のイラスト入りでお願いします。イラストはご自身で書いてくださってもいいですし、フリー素材でも構いません。
色合いは当院ホームページを参考にしてください。
当院ホームページ https://temuzeku.com/

記載する内容については、添付ファイルを参照してください。
ロゴデータは当選決定後に送らせて頂きます。

納品は、元データ(aiファイルやpsdファイル)とPNG書き出しでお願いします。

■重視する点
過去・現在までにデザインの経験のある方を希望致します。

その他何かご不明な点がございましたら、お気軽にご質問下さい。
よろしくお願いいたします。

文字が大きく読みやすい、温かみのあるデザインです。

皆さま、この度は当コンペにご参加いただき、誠にありがとうございます。
どれも力作で魅力的で選ぶのが大変でした。
今後ともどうぞよろしくお願いします。

```html
<!DOCTYPE html>
<html lang="ja">
<head>
<meta charset="utf-8">
<title>インフルエンザ予防接種</title>
<link href="https://fonts.googleapis.com/css2?family=M+PLUS+Rounded+1c:wght@500;700;800;900&display=swap" rel="stylesheet">
<style>
:root{
  --green:#5aa83a;
  --green-dark:#2f7a2a;
  --green-pale:#e6f3d6;
  --mint:#cfe9b8;
  --orange:#f39a1e;
  --red:#e2421c;
  --text:#333;
  --cream:#fffdf3;
  --line:#b9d9a0;
}
*{margin:0;padding:0;box-sizing:border-box}
html,body{width:846px;height:1200px;overflow:hidden}
body{font-family:"M PLUS Rounded 1c",sans-serif;color:var(--text);background:#fff}
.poster{position:relative;width:846px;height:1200px;background:linear-gradient(180deg,#d7eec2 0%,#f3faea 26%,#fff 40%);overflow:hidden}
.title-band{position:absolute;left:110px;top:22px;width:626px;height:100px;background:#fff;border-radius:50px;border:5px solid var(--mint)}
.title{position:absolute;top:24px;width:100%;text-align:center;font-size:80px;line-height:96px;font-weight:900;color:var(--green-dark);letter-spacing:3px}
.yobo{position:absolute;top:136px;left:0;width:100%;display:flex;justify-content:center;gap:14px}
.yobo span{width:118px;height:118px;border-radius:50%;background:var(--orange);color:#fff;font-size:70px;font-weight:900;display:flex;align-items:center;justify-content:center;border:5px solid #fff;box-shadow:0 0 0 4px var(--orange)}
.illus{position:absolute}
.illus.doctor{left:12px;top:120px;width:112px;height:245px;border-radius:20px;background:linear-gradient(180deg,#f6e2cf,#dff0f6)}
.illus.nurse{right:12px;top:120px;width:112px;height:245px;border-radius:20px;background:linear-gradient(180deg,#f6e2cf,#f7dbe3)}
.illus.virus1{left:150px;top:110px;width:40px;height:40px;border-radius:50%;background:#7a6a84}
.illus.virus2{right:150px;top:105px;width:36px;height:36px;border-radius:50%;background:#7a6a84}
.start{position:absolute;top:268px;width:100%;text-align:center;font-size:38px;line-height:48px;font-weight:800;color:var(--red)}
.start small{font-size:28px}
.no-reserve{position:absolute;top:324px;left:200px;width:446px;height:50px;background:var(--green-dark);color:#fff;border-radius:10px;font-size:30px;font-weight:800;text-align:center;line-height:50px}
.notes{position:absolute;top:392px;left:40px;width:770px;list-style:none}
.notes li{position:relative;padding-left:32px;font-size:20px;font-weight:700;line-height:1.5;margin-bottom:6px}
.notes li::before{content:"";position:absolute;left:4px;top:7px;width:17px;height:17px;border-radius:50%;background:var(--green)}
.fee-table{position:absolute;top:650px;left:40px;width:766px;border-collapse:collapse;table-layout:fixed;background:var(--cream)}
.fee-table th{background:var(--green);color:#fff;font-size:22px;font-weight:800;height:42px;border:2px solid #fff}
.fee-table td{border:2px solid var(--line);vertical-align:middle;font-weight:700}
.age{padding:10px 14px;font-size:22px;font-weight:800}
.age .sep{border-top:2px dashed var(--line);margin:6px 0}
.age .cond{font-size:13px;line-height:1.5;font-weight:700}
.age .ask{font-size:12px;color:var(--red);margin-top:4px}
.period{text-align:center;font-size:18px;line-height:1.8}
.fee{text-align:center;font-size:32px;font-weight:900;color:var(--red);line-height:1.3}
.fee small{font-size:17px;color:var(--text)}
.subsidy{display:inline-block;background:#fff;border:2px solid var(--green);border-radius:30px;color:var(--green-dark);font-size:19px;padding:6px 14px;line-height:1.3;margin-bottom:8px}
.others{font-size:16px;color:var(--green-dark);text-align:center;margin-bottom:6px}
.age-row{display:flex;align-items:center;gap:10px;white-space:nowrap}
.illus.elder{position:static;margin:10px auto 0;width:190px;height:100px;border-radius:14px;background:linear-gradient(180deg,#f4e3cf,#e4efd9)}
.illus.family{position:static;flex:none;width:60px;height:70px;border-radius:12px;background:#f0e0cf}
.footer{position:absolute;bottom:0;left:0;width:100%;height:78px;background:var(--green-pale);display:flex;align-items:center;justify-content:flex-end;padding-right:60px;gap:14px}
.footer .info{position:absolute;left:40px;font-size:13px;color:#666}
.mark{width:32px;height:32px;border-radius:50%;background:var(--green)}
.clinic{font-size:28px;font-weight:800;color:var(--green-dark)}
</style>
</head>
<body>
<div class="poster">
  <div class="title-band"></div>
  <h1 class="title">インフルエンザ</h1>
  <div class="illus virus1" role="img" aria-label="ウイルスのイラスト"></div>
  <div class="illus virus2" role="img" aria-label="ウイルスのイラスト"></div>
  <div class="illus doctor" role="img" aria-label="白衣の男性医師のイラスト"></div>
  <div class="illus nurse" role="img" aria-label="看護師のイラスト"></div>
  <div class="yobo"><span>予</span><span>防</span><span>接</span><span>種</span></div>
  <p class="start">10月11日<small>(金)</small>から、はじまります。</p>
  <p class="no-reserve">予約は必要ありません。</p>
  <ul class="notes">
    <li>インフルエンザに対する抵抗力がつくまで約２週間かかり、その効果は約５ヶ月持続します。</li>
    <li>２回接種をご希望の方は、１回目接種から４週間後に２回目接種を行います。</li>
    <li>肺炎球菌ワクチンとの同時接種はできます。</li>
    <li>体温が37.5度以上、具合が悪い方は別の日に接種しましょう。</li>
    <li>当院では妊娠中の方も予防接種できます。</li>
  </ul>
  <table class="fee-table">
    <colgroup><col style="width:300px"><col style="width:236px"><col style="width:230px"></colgroup>
    <tr><th>年齢</th><th>期間</th><th>接種費用</th></tr>
    <tr style="height:240px">
      <td class="age">65 歳以上<div class="sep"></div>60 歳以上 65 歳未満
        <div class="cond">心臓・腎臓・肺に障害がある方(※)<br>HIV 感染による免疫不全の方</div>
        <div class="ask">※詳しくは医師にお尋ねください</div></td>
      <td class="period" rowspan="2">令和 1 年 10 月 11 日～<br>令和 1 年 12 月 31 日<div class="illus elder" role="img" aria-label="高齢の夫婦のイラスト"></div></td>
      <td class="fee"><span class="subsidy">相模原市公費<br>負担あり</span><br>¥1500<small>（1回）</small></td>
    </tr>
    <tr style="height:140px">
      <td class="age"><div class="others">上記以外の方</div><div class="age-row"><span class="illus family" role="img" aria-label="家族のイラスト"></span>13 歳以上 65 歳未満</div></td>
      <td class="fee">¥4000<small>（1回目）</small><br>¥3000<small>（2回目）</small></td>
    </tr>
  </table>
  <div class="footer">
    <p class="info">診療時間 9:00～18:00 日曜休診</p>
    <span class="mark"></span><span class="clinic">緑町内科クリニック</span>
  </div>
</div>
</body>
</html>
```